Melissa Dorvan Personal Business Card

I like orange. It's would better if my card have an orange background
Address: 5820 Halvers Lane #417
San Jose
California
US
Tel: 4085172049

Industry/Entity Type

Business

```html
<!DOCTYPE html>
<html lang="en">
<head>
<meta charset="utf-8">
<title>Melissa Dorvan — Business Card</title>
<link rel="stylesheet" href="https://fonts.googleapis.com/css2?family=Open+Sans:wght@400;700&family=Dancing+Script:wght@500&display=swap">
<style>
  :root {
    --orange: #dd4726;
    --white: #ffffff;
    --stage: #151515;
    --band: #000000;
    --text-light: #ffffff;
  }
  * { margin: 0; padding: 0; box-sizing: border-box; }
  html, body { width: 1200px; height: 992px; overflow: hidden; background: var(--stage); }
  .canvas { position: relative; width: 1200px; height: 992px; background: var(--stage); font-family: "Open Sans", sans-serif; }

  .card { position: absolute; width: 500px; height: 286px; overflow: hidden; }
  .card--front { left: 70px; top: 240px; background: var(--orange); }
  .card--back  { left: 630px; top: 240px; background: var(--white); }

  .front-content { position: absolute; left: 130px; top: 104px; display: flex; align-items: flex-start; color: var(--text-light); }
  .wordmark { font-family: "Open Sans", sans-serif; font-weight: 700; font-size: 40px; line-height: 1; letter-spacing: -1px; color: var(--text-light); }
  .divider { width: 2px; height: 52px; background: var(--text-light); margin: 0 10px 0 8px; opacity: .85; }
  .details { padding-top: 2px; }
  .details__name { font-family: "Dancing Script", cursive; font-weight: 500; font-size: 27px; line-height: 1.05; letter-spacing: 1px; }
  .details__line { font-size: 11px; line-height: 1.4; letter-spacing: .3px; }
  .details__line--indent { padding-left: 46px; }

  .back-bar { position: absolute; background: var(--orange); }
  .back-bar--top { right: 0; top: 0; width: 130px; height: 24px; }
  .back-bar--bottom { left: 0; bottom: 0; width: 130px; height: 24px; }
  .back-mark { position: absolute; inset: 0; display: flex; align-items: center; justify-content: center; font-weight: 700; font-size: 150px; letter-spacing: -6px; color: var(--orange); line-height: 1; }

  .band { position: absolute; left: 0; top: 782px; width: 1200px; height: 210px; background: var(--band); }
  .band__mark { position: absolute; left: 78px; top: 20px; font-weight: 700; font-size: 150px; letter-spacing: -6px; color: var(--orange); line-height: 1; }

  .mini { position: absolute; width: 232px; height: 150px; overflow: hidden; }
  .mini--back { left: 728px; top: 40px; background: var(--white); }
  .mini--back .back-bar--top, .mini--back .back-bar--bottom { width: 60px; height: 12px; }
  .mini--back .back-mark { font-size: 64px; letter-spacing: -3px; justify-content: flex-start; padding-left: 56px; }
  .mini--front { left: 912px; top: 18px; width: 236px; height: 150px; background: var(--orange); transform: rotate(-9deg); box-shadow: -6px 6px 14px rgba(0,0,0,.5); }
  .mini--front .front-content { left: 54px; top: 56px; }
  .mini--front .wordmark { font-size: 18px; letter-spacing: 0; }
  .mini--front .divider { height: 26px; width: 1px; margin: 0 5px 0 4px; }
  .mini--front .details__name { font-size: 13px; }
  .mini--front .details__line { font-size: 5px; }
  .mini--front .details__line--indent { padding-left: 22px; }
</style>
</head>
<body>
<main class="canvas">
  <section class="card card--front" aria-label="Card front">
    <div class="front-content">
      <span class="wordmark">MD</span>
      <span class="divider"></span>
      <div class="details">
        <p class="details__name">Melissa Dorvan</p>
        <p class="details__line">Address: 5820 Halvers Lane #417</p>
        <p class="details__line details__line--indent">San Jose California US</p>
        <p class="details__line">Contact: 4085172049</p>
      </div>
    </div>
  </section>

  <section class="card card--back" aria-label="Card back">
    <span class="back-bar back-bar--top"></span>
    <span class="back-bar back-bar--bottom"></span>
    <div class="back-mark">MD</div>
  </section>

  <section class="band" aria-label="Identity summary">
    <div class="band__mark">MD</div>

    <div class="mini mini--back">
      <span class="back-bar back-bar--top"></span>
      <span class="back-bar back-bar--bottom"></span>
      <div class="back-mark">MD</div>
    </div>

    <div class="mini mini--front">
      <div class="front-content">
        <span class="wordmark">MD</span>
        <span class="divider"></span>
        <div class="details">
          <p class="details__name">Melissa Dorvan</p>
          <p class="details__line">Address: 5820 Halvers Lane #417</p>
          <p class="details__line details__line--indent">San Jose California US</p>
          <p class="details__line">Contact: 4085172049</p>
        </div>
      </div>
    </div>
  </section>
</main>
</body>
</html>
```